Rebranding Website – Tamsel Health Institute (40 Years)

Organization Description:
The Tamsel Health Institute (THI / www.tamselhi.nl) has been a trusted address for more than 40 years for people who choose a natural and sustainable approach to their health. We combine experience and history with a modern, professional approach.

Assignment:
Our current website is outdated and no longer reflects who we are today. We are looking for a new web design that aligns with our renewed logo and is both functional and inspiring. The website should have a clear structure, be user-friendly, and convey trust.

What we are looking for in the design:

A modern, fresh look that matches our logo and color palette logo in attachment.

Goal-oriented: simple and intuitive appointment scheduling.

Informative: space for a blog/news section to share knowledge and updates.

A dedicated page for each therapist with photo, expertise, and contact options.

A separate page for each type of therapy, with explanations and benefits.

A clear and visible link to our webshop (separate website).

Clear navigation and an organized menu structure.

Responsive design (desktop, tablet, mobile).

User-friendly CMS so we can manage and expand content ourselves.

Style Preferences:

- Color palette in line with our logo (green and natural tones, complemented by fresh and calm accents).
- Clean, professional design with plenty of white space.
- Accessible, warm, and inviting.

Functionalities:
- Online appointment scheduling or easy contact options.
- Blog/news section.
- Dedicated pages for therapists and therapies.
- Link to webshop.
- Possibility to expand the offer in the future (e.g., videos, downloads, or e-consultations).

What we would like to avoid:
- Pages that are too cluttered or confusing.
- Excessive text without clear structure.
- Stock photos lacking authenticity.

Target Audience:
People who consciously focus on their health, choose a natural approach, and are looking for a professional and reliable center where expertise and personal attention are central.

Additional Information:
The new website should bridge our 40-year history with the future. A place where visitors feel both familiar and inspired – and where they are immediately invited to get in touch, book an appointment, or visit our webshop.

You find our logo and impression in the uploads.

```html
<!DOCTYPE html>
<html lang="en">
<head>
<meta charset="utf-8">
<title>Tamsel Health Institute</title>
<link href="https://fonts.googleapis.com/css2?family=Poppins:wght@400;500;600;700&display=swap" rel="stylesheet">
<style>
:root{
  --green:#b3c91a;
  --green-dark:#9fb313;
  --navy:#272e3b;
  --card:#3b4656;
  --ink:#1f2430;
  --muted:#4a4f5a;
  --light:#f5f5f5;
  --grey:#ececec;
  --white:#ffffff;
}
*{box-sizing:border-box;margin:0;padding:0}
html,body{width:1200px;height:4329px;overflow:hidden}
body{font-family:"Poppins",sans-serif;color:var(--ink);background:var(--white);position:relative}
.abs{position:absolute}
.accent{color:var(--green)}
.btn{position:absolute;background:var(--green);color:var(--white);font-weight:600;font-size:15px;letter-spacing:.5px;border-radius:30px;display:flex;align-items:center;justify-content:center;text-transform:uppercase}
.section-title{position:absolute;font-size:32px;font-weight:500;letter-spacing:1px;text-transform:uppercase}
.lead{position:absolute;font-size:15px;color:var(--muted);text-align:center;width:1200px;left:0}
.photo{position:absolute}
/* hero */
.menu-btn{left:75px;top:35px;width:47px;height:47px;border-radius:8px;background:#eef2c8}
.hero-kicker{left:75px;top:138px;font-size:35px;font-weight:400;letter-spacing:1px}
.hero-title{left:75px;top:178px;font-size:45px;font-weight:500;line-height:52px}
.hero-text{left:75px;top:298px;width:500px;font-size:17px;line-height:26px;color:var(--ink)}
.hero-logo{left:735px;top:193px;width:195px;height:195px;border-radius:50%;background:var(--white);border:5px solid var(--green);display:flex;align-items:center;justify-content:center;font-size:50px;font-weight:600;color:var(--ink)}
/* about */
.about-card{left:75px;top:498px;width:1050px;height:462px;background:var(--light);border-radius:16px}
.about-title{left:532px;top:556px;font-size:31px;font-weight:500;line-height:38px;text-transform:uppercase}
.about-text{left:532px;top:652px;width:570px;font-size:15px;line-height:26.5px;color:var(--muted)}
/* therapies */
.therapy{position:absolute;top:1098px;width:328px;height:277px;border-radius:8px;background:var(--card);color:var(--white);text-align:center}
.therapy.active{background:var(--green)}
.therapy .icon{width:84px;height:84px;border-radius:50%;border:3px solid var(--green);margin:34px auto 0}
.therapy.active .icon{border-color:var(--ink)}
.therapy h3{font-size:17px;font-weight:600;margin-top:24px;letter-spacing:.5px}
.therapy p{font-size:14.5px;line-height:24px;margin:6px auto 0;width:275px;color:#e3e6ea}
.therapy.active p{color:#f6f9e0}
/* therapists */
.person{position:absolute;top:1660px;width:270px;text-align:center}
.person h4{font-size:17px;font-weight:600;margin-top:18px}
.person p{font-size:15px;line-height:22px;color:var(--muted);width:200px;margin:4px auto 0}
.socials{display:flex;gap:14px;justify-content:center;margin-top:12px}
.socials span{width:16px;height:16px;border-radius:3px;background:var(--green)}
/* webshop */
.shop-bg{left:0;top:2120px;width:616px;height:388px;background:var(--grey)}
.shop-text{left:76px;top:2250px;width:520px;font-size:15px;line-height:26.5px;color:var(--muted)}
/* blog */
.post{position:absolute;top:2692px;width:328px}
.post .img{height:222px;border-radius:4px}
.post h4{font-size:17px;font-weight:600;line-height:25px;margin-top:22px;text-transform:uppercase}
.post p{font-size:15px;line-height:26px;color:var(--muted);margin-top:10px}
.post a{font-size:13.5px;font-weight:600;color:var(--green);text-decoration:underline;display:block;margin-top:4px}
/* booking */
.field{position:absolute;background:var(--white);border-radius:26px;font-size:14px;color:var(--ink);padding:18px 22px 0;border:1px solid #d9dbe0}
/* footer */
.foot-h{position:absolute;font-size:15px;font-weight:600;color:var(--white);letter-spacing:.5px;text-transform:uppercase}
.foot-list{position:absolute;font-size:15px;line-height:30.5px;color:var(--white);list-style:none}
.foot-logo{left:118px;top:4035px;width:165px;height:165px;border-radius:50%;border:3px solid var(--white);display:flex;align-items:center;justify-content:center;font-size:42px;font-weight:600;color:var(--white)}
.copyright{left:0;top:4280px;width:1200px;text-align:center;font-size:14px;color:var(--white)}
</style>
</head>
<body>

<!-- Background shapes -->
<svg class="abs" style="left:0;top:0" width="1200" height="4329" viewBox="0 0 1200 4329">
  <defs>
    <linearGradient id="leafy" x1="0" y1="0" x2="1" y2="1">
      <stop offset="0" stop-color="#2f4a2b"/><stop offset="1" stop-color="#6e8a52"/>
    </linearGradient>
  </defs>
  <!-- hero photo area -->
  <path d="M440 0 H1200 V310 C1100 330 1010 300 940 250 C860 190 760 220 700 180 C600 120 520 60 440 0 Z" fill="url(#leafy)" role="img" aria-label="Garden greenery with stone statue"/>
  <!-- dark band -->
  <path d="M0 960 C100 900 300 980 700 930 C1000 890 1120 860 1200 800 V1453 H0 Z" fill="var(--navy)"/>
  <!-- booking wave -->
  <path d="M0 3250 C150 3130 300 3140 500 3180 C720 3225 880 3060 1200 3160 V3900 H0 Z" fill="var(--navy)"/>
  <!-- footer green -->
  <path d="M0 3990 C120 3860 250 3800 420 3800 C620 3800 760 3830 900 3870 C1030 3905 1120 3890 1200 3860 V4329 H0 Z" fill="var(--green)"/>
  <line x1="0" y1="4262" x2="1200" y2="4262" stroke="#c9da55" stroke-width="1"/>
</svg>

<!-- Hero -->
<div class="abs menu-btn">
  <svg width="47" height="47" viewBox="0 0 47 47"><g stroke="var(--ink)" stroke-width="2.5"><line x1="17" y1="18" x2="30" y2="18"/><line x1="17" y1="23.5" x2="30" y2="23.5"/><line x1="17" y1="29" x2="30" y2="29"/></g></svg>
</div>
<div class="abs hero-kicker">WELCOME TO</div>
<h1 class="abs hero-title">The Tamsel Health<br><span class="accent">Institute</span></h1>
<p class="abs hero-text">Excepteur sint occaecat cupidatat non proidentunt in culpa qui officia deserunt mollit anim.</p>
<div class="btn" style="left:75px;top:372px;width:284px;height:53px">Book an appointment</div>
<div class="abs hero-logo">THI</div>

<!-- About -->
<div class="abs about-card"></div>
<svg class="abs" style="left:105px;top:520px" width="400" height="420" viewBox="0 0 400 420">
  <defs><linearGradient id="por1" x1="0" y1="0" x2="0" y2="1"><stop offset="0" stop-color="#7c8b62"/><stop offset="1" stop-color="#e9e6df"/></linearGradient></defs>
  <circle cx="195" cy="215" r="162" fill="url(#por1)" role="img" aria-label="Portrait of a smiling practitioner in a white coat"/>
  <path d="M60 130 A170 170 0 1 1 120 370" fill="none" stroke="var(--green)" stroke-width="8" stroke-linecap="round"/>
</svg>
<h2 class="abs about-title">About Tamsel<br>Health <span class="accent">Institute</span></h2>
<p class="abs about-text">Nemo enim ipsam voluptatem quia voluptas sit aspernatur aut odit aut fugit, sed quia consequuntur magni dolores eos qui ratione voluptatem sequi nesciunt. Neque porro quisquam est, qui dolorem ipsum quia dolor sit amet, consectetur, adipisci velit, sed quia non numquam eius modi tempora incidunt ut labore et dolore magnam aliquam quaerat voluptatem.</p>
<div class="btn" style="left:532px;top:840px;width:166px;height:55px">Read more</div>

<!-- Therapies -->
<h2 class="section-title" style="left:75px;top:1028px;color:var(--white)">Our <span class="accent">Therapies</span></h2>
<svg class="abs" style="left:1065px;top:1035px" width="60" height="30" viewBox="0 0 60 30">
  <polyline points="13,5 5,15 13,25" fill="none" stroke="var(--white)" stroke-width="2.5"/>
  <polyline points="47,5 55,15 47,25" fill="none" stroke="var(--green)" stroke-width="2.5"/>
</svg>
<div class="therapy" style="left:75px"><div class="icon"></div><h3>ACUPUNCTURE THERAPY</h3><p>Nemo enim ipsam voluptatem quia voluptas sit aspernatur aut odit aut fugit, sed quia conse.</p></div>
<div class="therapy active" style="left:436px"><div class="icon"></div><h3>HOMEOPATHY</h3><p>Nemo enim ipsam voluptatem quia voluptas sit aspernatur aut odit aut fugit, sed quia conse.</p></div>
<div class="therapy" style="left:797px"><div class="icon"></div><h3>NATUROPATHY</h3><p>Nemo enim ipsam voluptatem quia voluptas sit aspernatur aut odit aut fugit, sed quia conse.</p></div>

<!-- Therapists -->
<h2 class="section-title" style="left:0;width:1200px;text-align:center;top:1515px">Our <span class="accent">Therapists</span></h2>
<p class="lead" style="top:1572px">Nemo enim ipsam voluptatem quia voluptas sit aspernatur aut odit aut fugit, sed quia consequuntur magni .</p>

<svg class="abs" style="left:0;top:1670px" width="1200" height="260" viewBox="0 0 1200 260">
  <defs><linearGradient id="por2" x1="0" y1="0" x2="0" y2="1"><stop offset="0" stop-color="#8a9180"/><stop offset="1" stop-color="#eef0f2"/></linearGradient></defs>
  <g>
    <circle cx="195" cy="130" r="112" fill="url(#por2)" role="img" aria-label="Portrait of a male therapist"/>
    <path d="M80 120 A118 118 0 1 0 195 12" fill="none" stroke="#c7c9cc" stroke-width="6"/>
  </g>
  <g>
    <circle cx="465" cy="130" r="112" fill="url(#por2)" role="img" aria-label="Portrait of a female therapist"/>
    <path d="M350 120 A118 118 0 1 0 465 12" fill="none" stroke="var(--green)" stroke-width="6"/>
  </g>
  <g>
    <circle cx="735" cy="130" r="112" fill="url(#por2)" role="img" aria-label="Portrait of a senior female therapist"/>
    <path d="M620 120 A118 118 0 1 0 735 12" fill="none" stroke="#c7c9cc" stroke-width="6"/>
  </g>
  <g>
    <circle cx="1005" cy="130" r="112" fill="url(#por2)" role="img" aria-label="Portrait of a female therapist with stethoscope"/>
    <path d="M890 120 A118 118 0 1 0 1005 12" fill="none" stroke="#c7c9cc" stroke-width="6"/>
  </g>
</svg>
<div class="person" style="left:60px;top:1925px"><h4>NAME HEADING</h4><p>Nemo enim ipsam volupt atem quia volu</p><div class="socials"><span></span><span></span><span></span></div></div>
<div class="person" style="left:330px;top:1925px"><h4>NAME HEADING</h4><p>Nemo enim ipsam volupt atem quia volu</p><div class="socials"><span></span><span></span><span></span></div></div>
<div class="person" style="left:600px;top:1925px"><h4>NAME HEADING</h4><p>Nemo enim ipsam volupt atem quia volu</p><div class="socials"><span></span><span></span><span></span></div></div>
<div class="person" style="left:870px;top:1925px"><h4>NAME HEADING</h4><p>Nemo enim ipsam volupt atem quia volu</p><div class="socials"><span></span><span></span><span></span></div></div>

<!-- Webshop -->
<div class="abs shop-bg"></div>
<div class="photo" style="left:616px;top:2120px;width:584px;height:388px;background:linear-gradient(135deg,#3f5a2c,#7f9a4f 55%,#8a5a2a)" role="img" aria-label="Herbs, mortar and pestle and tincture bottles in a garden"></div>
<h2 class="section-title" style="left:76px;top:2190px">Our <span class="accent">Webshop</span></h2>
<p class="abs shop-text">Nemo enim ipsam voluptatem quia voluptas sit aspernatur aut odit aut fugit, sed quia consequuntur magni dolores eos qui ratione voluptatem sequi nesciunt. Neque porro quisquam est, qui dolorem ipsum quia dolor sit amet, consectetur.</p>
<div class="btn" style="left:77px;top:2373px;width:181px;height:54px">Visit our shop</div>

<!-- Blog -->
<h2 class="section-title" style="left:0;width:1200px;text-align:center;top:2577px">Latest <span class="accent">Blog</span></h2>
<p class="lead" style="top:2636px">Nemo enim ipsam voluptatem quia voluptas sit aspernatur aut odit aut fugit, sed quia consequuntur magni .</p>
<div class="post" style="left:74px"><div class="img" style="background:linear-gradient(135deg,#c9c2b4,#8f9a7a)" role="img" aria-label="Consultation with fresh vegetables on the table"></div><h4>Duis aute irure dolor in reprehenderit</h4><p>Nemo enim ipsam voluptatem quia voluptas sit aspernatur aut odit aut fugit</p><a>Read More</a></div>
<div class="post" style="left:436px"><div class="img" style="background:linear-gradient(135deg,#e8e4de,#aebfc4)" role="img" aria-label="Practitioner showing a remedy bottle to a client"></div><h4>Duis aute irure dolor in reprehenderit</h4><p>Nemo enim ipsam voluptatem quia voluptas sit aspernatur aut odit aut fugit</p><a>Read More</a></div>
<div class="post" style="left:798px"><div class="img" style="background:linear-gradient(135deg,#f0f0ee,#9fc3d4)" role="img" aria-label="Acupuncture treatment in a clinic"></div><h4>Duis aute irure dolor in reprehenderit</h4><p>Nemo enim ipsam voluptatem quia voluptas sit aspernatur aut odit aut fugit</p><a>Read More</a></div>

<!-- Booking -->
<h2 class="section-title" style="left:74px;top:3330px;color:var(--white)">Book an <span class="accent">Appointment</span></h2>
<div class="field" style="left:76px;top:3392px;width:268px;height:54px">Name</div>
<div class="field" style="left:356px;top:3392px;width:268px;height:54px">Email Address</div>
<div class="field" style="left:76px;top:3461px;width:268px;height:54px">Phone No</div>
<div class="field" style="left:356px;top:3461px;width:268px;height:54px">Subject</div>
<div class="field" style="left:74px;top:3530px;width:550px;height:126px;border-radius:12px">Message</div>
<div class="btn" style="left:77px;top:3670px;width:181px;height:54px">Submit</div>
<svg class="abs" style="left:660px;top:3280px" width="440" height="460" viewBox="0 0 440 460">
  <defs><linearGradient id="por3" x1="0" y1="0" x2="0" y2="1"><stop offset="0" stop-color="#8a6a4a"/><stop offset="1" stop-color="#f2eee8"/></linearGradient></defs>
  <circle cx="245" cy="230" r="195" fill="url(#por3)" role="img" aria-label="Portrait of a smiling therapist in a pharmacy"/>
  <path d="M70 150 A205 205 0 1 1 175 425" fill="none" stroke="var(--green)" stroke-width="8" stroke-linecap="round"/>
</svg>

<!-- Footer -->
<div class="abs foot-logo">THI</div>
<div class="foot-h" style="left:355px;top:3982px">Quick Links</div>
<ul class="foot-list" style="left:355px;top:4008px"><li>Home</li><li>About Us</li><li>Therapies</li><li>Therapists</li><li>Testimonials</li><li>Blog</li><li>Contact Us</li></ul>
<div class="foot-h" style="left:587px;top:3982px">Contact Info</div>
<ul class="foot-list" style="left:587px;top:4008px;line-height:24px"><li>Lindeboomlaan 14</li><li>8441 KP Tamsel</li><li style="margin-top:6px">0513 480 219</li><li style="margin-top:6px">info@tamselhi.nl</li></ul>
<div class="foot-h" style="left:587px;top:4143px">Follow Us</div>
<div class="abs" style="left:584px;top:4180px;display:flex;gap:18px">
  <span style="width:20px;height:20px;border-radius:50%;border:2px solid var(--white)" aria-label="Social profile"></span>
  <span style="width:20px;height:20px;border-radius:50%;border:2px solid var(--white)" aria-label="Social profile"></span>
  <span style="width:20px;height:20px;border-radius:50%;border:2px solid var(--white)" aria-label="Social profile"></span>
  <span style="width:20px;height:20px;border-radius:50%;border:2px solid var(--white)" aria-label="Social profile"></span>
  <span style="width:20px;height:20px;border-radius:50%;border:2px solid var(--white)" aria-label="Social profile"></span>
</div>
<div class="foot-h" style="left:883px;top:3982px">Newsletter Subscribe</div>
<p class="abs" style="left:883px;top:4010px;width:240px;font-size:15px;line-height:23px;color:#eef4c4">Duis aute irure dolor in repre henderit in voluptate</p>
<div class="field" style="left:882px;top:4077px;width:241px;height:48px;padding-top:14px;font-size:13px;border:none">Email Address</div>
<div class="abs" style="left:882px;top:4139px;width:241px;height:46px;border-radius:24px;background:var(--navy);color:var(--white);font-weight:600;font-size:17px;display:flex;align-items:center;justify-content:center">Subscribe</div>
<div class="abs copyright">Copyright © 2025 Tamsel Health Institute All Right Reserved</div>

</body>
</html>
```